Jewelry Business card for general purpose. Elegant and simple

We are a jewelry group with 6 stores in Mexico and 30 years in business.

We need a BC that at leats includes the name, mail, phone number and physical location (street, municipality, and county; example "Paseo Arboleda 2140", "Avenida Quelites", "Valdoria").
Optional: we are trying to reposition the brand with the association of life-events or moments and family. Such as: birth, marriage, graduation, birthdays. Christmast, mothers day and fathers day.

We are looking for something elegant but simple

Jewelry name: "Lumora". Email: "lumoradesa@velmino.com". Phone num "4172-6395".

Target Market(s)

General business card: from suppliers to clients. One segment outstand: couples gettineg married

Industry/Entity Type

Jewelry Store

Contact Information for Business Card

Loking for something simple but elegant.

Font styles to use
Decorative
Script

Requirements
Must have
• Must have name, address, and mail.
Nice to have
• It could have jewelry pictures/design. Maybe quotes. Or general words as background . currently we have a very simple card with one ring would like to see something different.
Should not have
• Include real people.

```html
<!DOCTYPE html>
<html lang="es">
<head>
<meta charset="utf-8">
<title>Joyería Lumora – Tarjeta de presentación</title>
<link rel="stylesheet" href="https://fonts.googleapis.com/css2?family=Pinyon+Script&family=Open+Sans:wght@500;600&display=swap">
<style>
  :root {
    --paper: #ffffff;
    --onyx: #231f20;
    --gold-deep: #b8862e;
    --gold-mid: #d9b04a;
    --gold-light: #fff38a;
    --gold-warm: #f5c631;
    --ink: #141012;
    --script: "Pinyon Script", cursive;
    --sans: "Open Sans", sans-serif;
  }
  html, body {
    margin: 0;
    padding: 0;
    width: 1200px;
    height: 738px;
    overflow: hidden;
    background: var(--paper);
  }
  .business-card {
    position: relative;
    width: 1200px;
    height: 738px;
  }
  .card-shapes {
    position: absolute;
    inset: 0;
  }
  .brand-title {
    position: absolute;
    left: 74px;
    top: 212px;
    margin: 0;
    font-family: var(--script);
    font-weight: 400;
    font-size: 72px;
    line-height: 1;
    color: var(--ink);
    white-space: nowrap;
  }
  .contact-list {
    position: absolute;
    left: 70px;
    width: 480px;
    top: 372px;
    margin: 0;
    padding: 0;
    list-style: none;
    text-align: center;
    font-family: var(--sans);
    font-weight: 600;
    font-size: 24px;
    line-height: 45.5px;
    color: var(--ink);
    white-space: nowrap;
  }
  .brand-mark {
    position: absolute;
    left: 924px;
    top: 250px;
    transform: translate(-50%, -50%);
    display: flex;
    align-items: center;
    gap: 16px;
    font-family: var(--script);
    font-size: 64px;
    line-height: 1;
    color: var(--gold-mid);
    white-space: nowrap;
  }
  .brand-mark-dot {
    width: 22px;
    height: 22px;
    border-radius: 50%;
    background: var(--gold-mid);
  }
</style>
</head>
<body>
<main class="business-card">
  <svg class="card-shapes" width="1200" height="738" viewBox="0 0 1200 738" aria-hidden="true">
    <defs>
      <linearGradient id="gold-sweep" x1="0" y1="0" x2="1" y2="0">
        <stop offset="0" stop-color="var(--gold-deep)"/>
        <stop offset="0.35" stop-color="var(--gold-mid)"/>
        <stop offset="0.72" stop-color="var(--gold-light)"/>
        <stop offset="1" stop-color="var(--gold-warm)"/>
      </linearGradient>
    </defs>
    <path class="card-base" fill="var(--onyx)"
          d="M0 738 V70 Q0 0 70 0 H1200 V620 Q1200 738 1082 738 Z"/>
    <path class="gold-sweep" fill="url(#gold-sweep)"
          d="M0 738 V100 Q0 30 58 30 C400 40 820 330 1040 738 Z"/>
  </svg>

  <h1 class="brand-title">Joyería Lumora</h1>

  <ul class="contact-list">
    <li>+00 417 263 9584</li>
    <li>lumoradesa@velmino.com</li>
    <li>www.lumorajoyas.com</li>
    <li>Paseo Arboleda 2140 Avenida Quelites</li>
    <li>Valdoria</li>
  </ul>

  <div class="brand-mark">
    <span class="brand-mark-dot"></span>
    <span class="brand-mark-name">Lumora</span>
  </div>
</main>
</body>
</html>
```